Pharmacy Benefit Manager needs grahics for marketing material

We have a logo. We need integrated graphics we can use for proposal cover sheets and a power point template. I am including our logo and our business cards. We do not want to use pills, prescription bottles or other pharmacy related objects.

Industry/Entity Type

Marketing

```html
<!DOCTYPE html>
<html lang="en">
<head>
<meta charset="utf-8">
<title>Lorem Ipsum – Presentation Slide</title>
<link rel="stylesheet" href="https://fonts.googleapis.com/css2?family=Arimo:wght@400;700&display=swap">
<style>
  :root {
    --backdrop: #ece7df;
    --slide-bg: #ffffff;
    --ink: #000000;
    --accent-green: #4e7a1e;
    --panel-black: #000000;
    --panel-green: #5b9632;
  }
  * { box-sizing: border-box; margin: 0; padding: 0; }
  html, body {
    width: 1200px;
    height: 1000px;
    overflow: hidden;
    background: var(--backdrop);
    font-family: "Arimo", Arial, sans-serif;
    color: var(--ink);
  }
  .slide {
    position: absolute;
    left: 146px;
    top: 195px;
    width: 925px;
    height: 638px;
    background: var(--slide-bg);
    overflow: hidden;
  }
  .side-graphic {
    position: absolute;
    left: 0;
    top: 0;
    width: 240px;
    height: 638px;
  }
  .slide-title {
    position: absolute;
    left: 292px;
    top: 68px;
    font-size: 76px;
    font-weight: 700;
    line-height: 1;
    letter-spacing: -0.3px;
  }
  .slide-subtitle {
    position: absolute;
    left: 204px;
    top: 160px;
    font-size: 39px;
    font-weight: 400;
    line-height: 50px;
    letter-spacing: 1.3px;
  }
  .bullet-list {
    position: absolute;
    left: 204px;
    top: 283px;
    list-style: none;
    font-size: 25px;
    line-height: 35px;
    letter-spacing: 0.9px;
  }
  .bullet-list li { margin-bottom: 15px; }
  .bullet-list li::before { content: "\2022\00a0"; }
  .highlight { color: var(--accent-green); }
  .highlight--strong { font-weight: 700; }
  .brand {
    position: absolute;
    left: 712px;
    top: 558px;
    display: flex;
    align-items: center;
    gap: 10px;
    font-size: 40px;
    font-weight: 700;
    line-height: 1;
    color: var(--ink);
  }
  .brand-square {
    width: 22px;
    height: 22px;
    background: var(--ink);
  }
  .footer-rule {
    position: absolute;
    left: 122px;
    top: 619px;
    width: 781px;
    height: 2px;
    background: var(--ink);
  }
</style>
</head>
<body>
  <section class="slide">
    <svg class="side-graphic" viewBox="0 0 240 638" role="img" aria-label="Abstract curved grid graphic in green and black on the left edge of the slide">
      <defs>
        <linearGradient id="panelTone" x1="0" y1="0" x2="0" y2="1">
          <stop offset="0" stop-color="var(--panel-black)"/>
          <stop offset="0.3" stop-color="#111a08"/>
          <stop offset="0.5" stop-color="#3f6b22"/>
          <stop offset="0.7" stop-color="#1a2a0d"/>
          <stop offset="1" stop-color="var(--panel-black)"/>
        </linearGradient>
      </defs>
      <path d="M0 0 H226 C160 130 112 260 116 420 C118 500 120 570 122 638 H0 Z" fill="url(#panelTone)"/>
    </svg>

    <h1 class="slide-title">Lorem Ipsum</h1>
    <p class="slide-subtitle">Slidecraft presentation template<br>a really professional looking slide.</p>

    <ul class="bullet-list">
      <li><span class="highlight highlight--strong">Slidecraft</span> presentation template<br>a really professional looking slide.</li>
      <li>Slidecraft <span class="highlight">presentation</span> template<br>a really professional looking slide.</li>
      <li>Slidecraft presentation <span class="highlight">template</span><br>a really professional looking slide.</li>
    </ul>

    <div class="brand">
      <span class="brand-square"></span>
      <span class="brand-name">Verano</span>
    </div>

    <div class="footer-rule"></div>
  </section>
</body>
</html>
```